Gutschein-Design für Lorenzo Restaurant
Zielgruppe
Pizzeria Restaurant à la carte/ Das Design soll Jedem gefallen, mir, Familien, Pärchen, etc.
Aufgabenstellung
Die Gutscheine werden von unserem Kassensystem bedruckt. Die Größe ist ca. 95 mm/ 80 mm. Dieser Bon sollte in die Gutschein-Hülle, die ich jetzt brauche eingesteckt sein. Die Masse sollen 105x105 mm sein, offen 105x210 mm .
Text:
Auf Seite 1:
- Das Logo
- Geschenk-Gutschein
Auf Seite 2:
- Der Gutschein kann für Vieles gut sein
- In unserem Fall lässt unsere reichhaltige Karte viele Möglichkeiten offen
- Auf jeden Fall wird bestimmt geschlemmt, geschmaust und genossen
- Wir wünschen guten Appetit
Auf Seite 3 für die Druckerei:
- 2 Halbkreise gestanzt und 1x gerillt, rundum auf Endformat beschnitten.
- 1-Bruch Falz
Hier gehört der Gutschein-Bon 95/80 mm eingesteckt
Auf Seite 4:
Lorenzo
Restaurantbetriebsgesellschaft m.b.H.
www.lorenzo-trattoria.at
Im Dateiupload habe ich als ein Beispiel die jetzigen Gutscheinhuelle beigefügt.
MfG

```html
<!DOCTYPE html>
<html lang="de">
<head>
<meta charset="utf-8">
<title>Gutschein-Hülle – Innenseite</title>
<link rel="stylesheet" href="https://fonts.googleapis.com/css2?family=Lobster&display=swap">
<style>
  :root {
    --wine: #5a0000;
    --wine-fold: #520000;
    --gold: #ebdc86;
    --gold-edge: #e8b060;
    --blush: #d6a2a2;
    --paper: #ffffff;
  }
  * { margin: 0; padding: 0; box-sizing: border-box; }
  html, body { width: 1200px; height: 601px; overflow: hidden; background: var(--wine); }
  .spread { position: relative; width: 1200px; height: 601px; background: var(--wine); overflow: hidden; }
  .band { position: absolute; left: 0; width: 1200px; height: 17px; background: var(--gold); }
  .band--top { top: 37px; }
  .band--bottom { top: 556px; }
  .fold { position: absolute; left: 600px; top: 0; width: 3px; height: 601px; background: var(--wine-fold); }
  .fold::before, .fold::after { content: ""; position: absolute; left: 0; width: 3px; height: 17px; background: var(--gold-edge); }
  .fold::before { top: 37px; }
  .fold::after { top: 556px; }
  .page-inner-left {
    position: absolute; left: 0; top: 0; width: 600px; height: 601px;
    font-family: "Lobster", cursive; color: var(--gold); text-align: center;
  }
  .message { position: absolute; left: 0; width: 606px; white-space: nowrap; }
  .message__title { top: 92px; font-size: 34px; line-height: 40px; font-weight: 400; }
  .message__body { top: 136px; font-size: 24px; line-height: 36px; }
  .message__closing { top: 327px; font-size: 24.5px; line-height: 36px; }
  .table-photo {
    position: absolute; left: 163px; top: 399px; width: 274px; height: 156px;
    background: linear-gradient(135deg, #b8c4cc 0%, #9aa0a0 35%, #c9b870 60%, #3a2a26 80%, #2a1f1e 100%);
  }
  .pocket { position: absolute; left: 600px; top: 0; width: 600px; height: 601px; }
</style>
</head>
<body>
<main class="spread">
  <div class="band band--top"></div>
  <div class="band band--bottom"></div>

  <section class="page-inner-left">
    <h1 class="message message__title">Ein Gutschein</h1>
    <p class="message message__body">
      kann  für Vieles gut sein.<br>
      In unserem Fall lässt unsere<br>
      reichhaltige Karte viele Möglichkeiten offen.<br>
      Auf jeden Fall wird bestimmt  geschlemmt,<br>
      geschmaust und genossen.
    </p>
    <p class="message message__closing">Wir wünschen guten Appetit.</p>
    <div class="table-photo" role="img" aria-label="Foto: gedeckter Restauranttisch mit Weingläsern und gefalteter Serviette"></div>
  </section>

  <div class="fold"></div>

  <svg class="pocket" width="600" height="601" viewBox="600 0 600 601" aria-label="Einstecklasche für den Gutschein-Bon">
    <defs>
      <clipPath id="pocket-area">
        <rect x="628" y="72" width="542" height="456"/>
      </clipPath>
    </defs>
    <g clip-path="url(#pocket-area)">
      <rect x="628" y="72" width="542" height="456" fill="var(--paper)"/>
      <polygon points="628,72 1045,528 628,528" fill="var(--blush)"/>
    </g>
    <path d="M807 72 A85 85 0 0 0 977 72 Z" fill="var(--wine)"/>
    <path d="M806 528 A83 83 0 0 1 972 528 Z" fill="var(--wine)"/>
    <rect x="803" y="65" width="1.2" height="4" fill="var(--paper)"/>
    <rect x="981" y="65" width="1.2" height="4" fill="var(--paper)"/>
  </svg>
</main>
</body>
</html>
```